Non profit Haiti relief organization needs an invitation to a fundraising event

We need a catchy invitation for our 8th annual "Light the Lantern Onward" event. Our mission is to provide relief, hope and dignity to the poor, elderly and homeless people of Haiti. This direct mail piece will measure 5 x 7 and will be mailed to 3,000 supports and used for personal invitation. The invitation needs to include a photo of a wheel that we use every year, a photo of our founder, the late Fr. Clement Dusoll, one or two photos of the poor that we serve in Haiti, and our logo. I uploaded some photos, but photos from our website could also be used.

Text:
Providing relief, hope & dignity to the poor, elderly & homeless people of Haiti.
Education, Water, Food, Orphan Care, Elder Care

8th Annual "Light The Lantern Onward" Event
Wednesday, April 23, 2014 6pm
Gardens of Pellham, 27816 Fulton Ave SE, Pellham, MN

Live Auction, Marketplace, Music, Beverages, Appetizers

$5 Admission. Pay at the door.

Help us carry on Father Dusoll's legacy in Haiti.

www.dusollaidfund.org 612-947-5186

Dusoll Aid, Inc. is a 501(c)(3) non-profit organization. All donations tax deductible.

Target Market(s)

Adults who live in Minnesota, Christians

Industry/Entity Type

Non-Profit

Requirements
Must have
• The invitation must be 5 x 7 and have print on both sides. Must have text listed in project overview
Nice to have
• I included front and back images of the postcard that we used last year to give an idea of design that we've used in past.

```html
<!DOCTYPE html>
<html lang="en">
<head>
<meta charset="utf-8">
<title>Light The Lantern Onward — Invitation</title>
<link href="https://fonts.googleapis.com/css2?family=Oswald:wght@500&family=PT+Serif&family=Gochi+Hand&family=Montserrat:wght@500&display=swap" rel="stylesheet">
<style>
  :root {
    --orange: #e8832a;
    --navy: #2e3163;
    --teal: #5a9a98;
    --white: #ffffff;
    --ink: #2a2a2a;
  }
  html, body { margin: 0; padding: 0; overflow: hidden; background: var(--white); }
  .invitation {
    position: relative; width: 1200px; height: 857px; overflow: hidden;
    background: var(--white); font-family: "PT Serif", Georgia, serif;
  }
  .brand { position: absolute; left: 40px; top: 42px; width: 178px; text-align: center; }
  .brand-mark {
    width: 148px; height: 148px; margin: 0 auto; border-radius: 50%;
    border: 4px solid var(--teal); box-sizing: border-box;
  }
  .brand-name {
    margin-top: 10px; font-family: "Montserrat", sans-serif; font-weight: 500;
    font-size: 13px; letter-spacing: 2px; color: var(--teal); white-space: nowrap;
  }
  .mission {
    position: absolute; left: 249px; top: 103px; margin: 0;
    color: var(--navy); font-size: 23px; line-height: 33px;
  }
  .event-band {
    position: absolute; left: 0; top: 238px; width: 1200px; height: 229px;
    background: var(--orange);
  }
  .photo-frame {
    position: absolute; background: var(--white); padding: 9px;
    box-shadow: 0 2px 6px rgba(0,0,0,.35);
  }
  .photo-child { left: 70px; top: 248px; width: 162px; height: 192px; }
  .photo-founder {
    left: 82px; top: 628px; width: 145px; height: 160px; transform: rotate(-8deg);
  }
  .photo-fill { width: 100%; height: 100%; }
  .photo-child .photo-fill { background: linear-gradient(120deg, #2bb0b8 0%, #4fc4c4 45%, #6b4a3a 80%, #8a5a40 100%); }
  .photo-founder .photo-fill { background: linear-gradient(160deg, #5b4a3e 0%, #a89a8c 45%, #1c1c1e 100%); }
  .event-details {
    position: absolute; right: 138px; top: 257px; text-align: right;
    font-family: "Oswald", "Arial Narrow", sans-serif; font-weight: 500;
    color: var(--white); line-height: 1;
  }
  .event-title, .event-date { font-size: 37px; margin-bottom: 13px; }
  .event-venue { font-size: 31px; margin-bottom: 14px; }
  .highlights {
    position: absolute; left: 138px; top: 505px; margin: 0;
    font-family: "Gochi Hand", cursive; font-size: 40px; color: var(--navy); font-weight: 400;
  }
  .admission {
    position: absolute; right: 64px; top: 562px; margin: 0;
    font-family: "Gochi Hand", cursive; font-size: 52px; color: var(--navy); font-weight: 400;
  }
  .legacy-band {
    position: absolute; left: 0; top: 670px; width: 1200px; height: 112px;
    background: var(--orange);
  }
  .legacy {
    position: absolute; left: 252px; top: 688px; margin: 0;
    font-family: "Gochi Hand", cursive; font-size: 29px; line-height: 38px; color: var(--white);
  }
  .contact {
    position: absolute; right: 58px; top: 742px; margin: 0;
    font-size: 24px; color: var(--navy);
  }
  .legal {
    position: absolute; right: 60px; top: 818px; margin: 0;
    font-size: 15px; color: var(--ink);
  }
</style>
</head>
<body>
<main class="invitation">
  <header class="brand">
    <div class="brand-mark"></div>
    <div class="brand-name">DUSOLL AID INC</div>
  </header>
  <p class="mission">Providing relief, hope &amp; dignity to the poor, elderly &amp; homeless people of Haiti.<br>Education, Water, Food, Orphan Care, Elder Care</p>

  <section class="event-band"></section>
  <figure class="photo-frame photo-child" style="margin:0">
    <div class="photo-fill" role="img" aria-label="Photo of a young child in Haiti standing beside a turquoise corrugated metal wall"></div>
  </figure>
  <div class="event-details">
    <div class="event-title">8th Annual "Light The Lantern Onward" Event</div>
    <div class="event-date">Wednesday, April 23, 2014 6pm</div>
    <div class="event-venue">Gardens of Pellham,</div>
    <div class="event-venue">27816 Fulton Ave SE, Pellham, MN</div>
  </div>

  <h2 class="highlights">Live Auction, Marketplace, Music, Beverages, Appetizers</h2>
  <h2 class="admission">$5 Admission. Pay at the door.</h2>

  <section class="legacy-band"></section>
  <figure class="photo-frame photo-founder" style="margin:0">
    <div class="photo-fill" role="img" aria-label="Portrait photo of the late founder, Fr. Clement Dusoll"></div>
  </figure>
  <p class="legacy">Help us carry on Father Dusoll's<br>legacy in Haiti.</p>
  <p class="contact">www.dusollaidfund.org 612-947-5186</p>
  <p class="legal">Dusoll Aid, Inc. is a 501(c)(3) non-profit organization. All donations tax deductible.</p>
</main>
</body>
</html>
```